Business card for Autism Consultancy

I need a double-sided business card for Brightpath Learning Consultancy
Please try to use the colours and graphics in line with our website www.brightpathlearn.nz
Front side
Logo and the name of the company – Brightpath Learning Consultancy
We use Child-Centred, Modern and Innovative approaches
Teaching autistic children to bond, laugh and play
www.brightpathlearn.nz
info@brightpathlearn.nz
phone +64 09 37 615 48
Back side
Photo
Mirela Dunstan
Founder
Postgraduate Autism (Children) Specialist (with Merit)
Qualified by the Faculty of Learning Support and Access Studies (FLSA), Harwell Vale University
mirela@brightpathlearn.nz
phone +64 937 615 48
mobile: +64 20 6283 9150
Please do not convert the text fields to outlines, i.e. I need to be able to edit any text after.
The final design should be either in Adobe Illustrator or Adobe Photoshop format.
The Specs for the business card are:
Full Bleed Size
94 x 58 mm
1110 x 685 pixels
Document Trim Size
91 x 55 mm
1075 x 650 pixels

```html
<!DOCTYPE html>
<html lang="en">
<head>
<meta charset="utf-8">
<title>Brightpath Learning Consultancy – Business Card</title>
<link href="https://fonts.googleapis.com/css2?family=Lato:wght@400;700;900&display=swap" rel="stylesheet">
<style>
  :root {
    --navy: #1f2c5e;
    --navy-light: #27366d;
    --yellow: #f7d117;
    --white: #ffffff;
    --stage: #202020;
    --photo-warm: #c9a48a;
    --photo-light: #f4efe9;
  }
  * { margin: 0; padding: 0; box-sizing: border-box; }
  html, body {
    width: 1200px; height: 900px; overflow: hidden;
    background: var(--stage);
    font-family: "Lato", Arial, sans-serif;
  }
  .sheet {
    width: 1200px; height: 900px;
    display: flex; flex-direction: column; align-items: center; justify-content: center;
    gap: 30px;
  }
  .card {
    position: relative;
    width: 680px; height: 411px;
    background: linear-gradient(135deg, var(--navy) 0%, var(--navy-light) 60%, var(--navy) 100%);
    border-bottom: 6px solid var(--yellow);
    color: var(--white);
    overflow: hidden;
  }
  /* Brand name block */
  .brand {
    display: flex; align-items: center; gap: 14px;
  }
  .brand-mark {
    width: 34px; height: 34px; background: var(--yellow); flex: none;
  }
  .brand-name {
    font-weight: 700; color: var(--white); line-height: 1.1;
  }
  /* Front */
  .front .brand { position: absolute; left: 200px; top: 110px; }
  .front .brand-name { font-size: 30px; }
  .contact-list { list-style: none; }
  .contact-list li {
    display: flex; align-items: center; gap: 10px;
    line-height: 1.35;
  }
  .contact-list svg { width: 12px; height: 12px; flex: none; }
  .front .contact-list {
    position: absolute; left: 150px; top: 270px; font-size: 17px;
  }
  /* Back */
  .portrait {
    position: absolute; left: 60px; top: 65px;
    width: 236px; height: 236px; border-radius: 50%;
    border: 4px solid var(--yellow);
    background: radial-gradient(circle at 50% 42%, var(--photo-warm) 0%, #8a6a55 38%, var(--photo-light) 70%);
  }
  .divider {
    position: absolute; left: 350px; top: 70px;
    width: 3px; height: 280px; background: var(--yellow);
  }
  .back .brand { position: absolute; left: 380px; top: 60px; }
  .back .brand-mark { width: 28px; height: 28px; }
  .back .brand-name { font-size: 22px; }
  .profile { position: absolute; left: 380px; top: 160px; }
  .profile-name {
    font-size: 30px; font-weight: 700; color: var(--yellow);
    text-transform: uppercase; letter-spacing: 0.5px;
  }
  .profile-role { font-size: 17px; line-height: 1.3; margin-top: 4px; }
  .back .contact-list { margin-top: 14px; font-size: 17px; }
</style>
</head>
<body>
<main class="sheet">

  <section class="card front" aria-label="Card front">
    <div class="brand">
      <span class="brand-mark"></span>
      <span class="brand-name">Brightpath Learning<br>Consultancy</span>
    </div>
    <ul class="contact-list">
      <li>
        <svg viewBox="0 0 12 12"><path d="M2.5 1 L4.5 1 L5 3.5 L3.8 4.3 Q4.8 6.6 7.7 8.2 L8.5 7 L11 7.5 L11 9.5 Q10.5 11 9 11 Q2 9.5 1 3 Q1 1.5 2.5 1 Z" fill="var(--yellow)"/></svg>
        +64 09 37 615 48
      </li>
      <li>
        <svg viewBox="0 0 12 12"><rect x="1" y="2.5" width="10" height="7" fill="none" stroke="var(--yellow)" stroke-width="1.2"/><path d="M1 2.5 L6 6.5 L11 2.5" fill="none" stroke="var(--yellow)" stroke-width="1.2"/></svg>
        info@brightpathlearn.nz
      </li>
      <li>
        <svg viewBox="0 0 12 12"><circle cx="6" cy="6" r="5" fill="none" stroke="var(--yellow)" stroke-width="1.1"/><ellipse cx="6" cy="6" rx="2.2" ry="5" fill="none" stroke="var(--yellow)" stroke-width="1"/><path d="M1 6 H11" stroke="var(--yellow)" stroke-width="1"/></svg>
        www.brightpathlearn.nz
      </li>
    </ul>
  </section>

  <section class="card back" aria-label="Card back">
    <div class="portrait" role="img" aria-label="Portrait photo of Mirela Dunstan"></div>
    <div class="divider"></div>
    <div class="brand">
      <span class="brand-mark"></span>
      <span class="brand-name">Brightpath Learning<br>Consultancy</span>
    </div>
    <div class="profile">
      <h1 class="profile-name">Mirela Dunstan</h1>
      <p class="profile-role">Founder<br>Postgraduate Autism<br>(Children) Specialist (with Merit)</p>
      <ul class="contact-list">
        <li>
          <svg viewBox="0 0 12 12"><path d="M2.5 1 L4.5 1 L5 3.5 L3.8 4.3 Q4.8 6.6 7.7 8.2 L8.5 7 L11 7.5 L11 9.5 Q10.5 11 9 11 Q2 9.5 1 3 Q1 1.5 2.5 1 Z" fill="var(--yellow)"/></svg>
          +64 937 615 48
        </li>
        <li>
          <svg viewBox="0 0 12 12"><rect x="3" y="0.8" width="6" height="10.4" rx="1" fill="none" stroke="var(--yellow)" stroke-width="1.2"/><circle cx="6" cy="9.3" r="0.7" fill="var(--yellow)"/></svg>
          +64 20 6283 9150
        </li>
        <li>
          <svg viewBox="0 0 12 12"><rect x="1" y="2.5" width="10" height="7" fill="none" stroke="var(--yellow)" stroke-width="1.2"/><path d="M1 2.5 L6 6.5 L11 2.5" fill="none" stroke="var(--yellow)" stroke-width="1.2"/></svg>
          mirela@brightpathlearn.nz
        </li>
      </ul>
    </div>
  </section>

</main>
</body>
</html>
```